Agency Website & Personal brand

My name is Kostas Vranelis & I've been a digital marketer & an e-commerce expert since 2010.

- I've spoken to 20 different events around the world up to 3,000 people in size.
- I've sold over 1500 training courses around e-commerce growth.
- I have over 100 testimonials (video & photo) from successful students who bought my training
- I have dozens of video testimonials from respected entrepreneurs that vouch for me and my work
- I have photos with marketing legends with that I shared the stage like Owen Tarrick, Martin Fellowbrand, Glen Maro & more
- I am the host of the Aegean Roundtable since 2017 - a high-level networking event for 7 & 8 figure entrepreneurs - 100 people have come to Greece since 2017
- I have tons of videos created where I showcase my expertise on growth
- I have worked with dozens of e-commerce stores on their growth & helped them scale to multiple 6, 7 & 8 figures either on consulting

I need a website design that showcases my authority & be a lead generating machine.

The goal is to bring people on a call with me but also grab their email and start building the relationship with them and free valuable content

We have 3 offers :

1. Paid ads (Done for You)
2. Consulting/Mastermind (Done with You)
3. Training (Do it Yourself)

```html
<!DOCTYPE html>
<html lang="en">
<head>
<meta charset="utf-8">
<title>Kostas Vranelis — E-commerce Growth</title>
<link href="https://fonts.googleapis.com/css2?family=Poppins:wght@300;400;500&display=swap" rel="stylesheet">
<style>
:root{
  --green:#4f8a64;
  --green-light:#6aa57d;
  --dark:#1c1c1c;
  --darker:#111;
  --mint:#edf2ee;
  --card:#cbcdcb;
  --white:#fff;
  --ink:#111;
}
*{box-sizing:border-box;margin:0;padding:0}
html,body{width:1200px;height:3055px;overflow:hidden;background:var(--white);font-family:'Poppins',sans-serif;color:var(--ink)}
.abs{position:absolute}
.page{position:relative;width:1200px;height:3055px}

/* hero */
.hero{left:107px;top:0;width:911px;height:367px;background:linear-gradient(120deg,#2c3a33 0%,#1d1f1e 45%,#141414 100%)}
.hero-photo{left:0;top:0;width:911px;height:367px;background:radial-gradient(ellipse at 25% 60%,rgba(60,110,80,.45),transparent 55%),radial-gradient(ellipse at 75% 30%,rgba(90,90,90,.35),transparent 60%)}
.logo{font-weight:300;font-size:22px;color:var(--white);letter-spacing:1px}
.logo b{font-weight:300;color:var(--green-light)}
.nav a{position:absolute;top:22px;font-size:13px;color:var(--white);text-decoration:none;white-space:nowrap}
.nav a.active{color:var(--green-light)}
.hero h1{left:0;width:911px;top:108px;text-align:center;font-weight:300;font-size:37px;line-height:47px;color:var(--white)}
.hero .lead{left:0;width:911px;top:222px;text-align:center;font-weight:300;font-size:17px;color:var(--white)}
.hero .cta{left:273px;top:295px;width:405px;height:51px;border:1px solid rgba(255,255,255,.5);color:var(--white);font-size:13.5px;display:flex;align-items:center;justify-content:center;gap:22px}

/* newsletter */
.newsletter{background:var(--green);color:var(--white);text-align:center;overflow:hidden}
.newsletter .leaf{right:0;top:0;width:110px;height:100%;background:radial-gradient(ellipse at 80% 60%,rgba(255,255,255,.35),transparent 65%)}
.newsletter h3{font-weight:300;font-size:19px;margin-top:18px}
.newsletter p{font-weight:300;font-size:13.5px;line-height:21px;margin-top:6px}
.newsletter .form{display:flex;justify-content:center;margin-top:14px}
.newsletter .field{width:378px;height:34px;background:var(--white);color:#888;font-size:13.5px;text-align:left;padding:7px 11px}
.newsletter .btn{width:115px;height:34px;background:var(--darker);color:var(--white);font-size:15px;font-weight:300;padding-top:6px}

/* about */
.about{left:107px;top:583px;width:911px;height:383px;background:radial-gradient(ellipse at 80% 45%,#5e5e5e 0%,#2c2c2c 45%,#222 100%)}
.about h2{left:100px;top:42px;font-weight:400;font-size:35px;color:var(--green-light);letter-spacing:1px}
.about h2::after{content:"";position:absolute;left:183px;top:24px;width:92px;height:2px;background:var(--green-light)}
.facts li{position:absolute;left:114px;list-style:none;font-size:11.5px;line-height:20px;color:var(--white);font-weight:300;width:420px}
.facts li::before{content:"";position:absolute;left:-16px;top:10px;width:5px;height:5px;border-radius:50%;background:var(--green-light)}
.facts .hl{color:var(--green-light)}
.snap{background:linear-gradient(135deg,#7a6a55,#3d4a40);border:4px solid var(--white)}

/* offers */
.offers{left:187px;top:966px;width:752px;height:456px;background:var(--mint);text-align:center}
.offers h2{position:absolute;left:0;width:752px;top:26px;font-weight:400;font-size:26px}
.offers h2 span{color:var(--green)}
.offers h3{position:absolute;left:0;width:752px;top:66px;font-weight:400;font-size:25px;color:var(--green)}
.offer{position:absolute;top:132px;width:240px;text-align:center}
.offer svg{display:block;margin:0 auto}
.offer h4{font-weight:300;font-size:20.5px;line-height:30px;margin-top:10px}
.offer p{font-size:11.5px;line-height:19px;margin-top:12px}
.btn-green{background:var(--green);color:var(--white);font-size:15px;font-weight:300;display:flex;align-items:center;justify-content:center}

/* cases */
.cases{left:107px;top:1424px;width:911px;height:709px;background:radial-gradient(ellipse at 70% 10%,#4a4a4a,#161616 55%,#111 100%)}
.cases h2{left:109px;top:36px;font-weight:400;font-size:37px;color:var(--white)}
.cases h2::after{content:"";position:absolute;left:240px;top:28px;width:92px;height:2px;background:var(--white)}
.cases .intro{left:109px;top:86px;font-size:13.5px;line-height:20px;color:var(--white);font-weight:300}
.case{position:absolute;top:183px;width:178px;text-align:center;color:var(--white)}
.case .img{height:233px;border:1px solid #aaa}
.case h4{font-weight:400;font-size:24px;color:var(--green-light);margin-top:16px}
.case p{font-size:16px;line-height:23px;font-weight:300;margin-top:6px}

/* testimonials */
.clients-title{left:0;width:1130px;top:2200px;text-align:center;font-weight:400;font-size:37px}
.review{left:187px;width:752px;height:158px;background:linear-gradient(90deg,#dde2dc,#c6c7c5)}
.review .avatar{left:30px;top:30px;width:98px;height:98px;border-radius:50%;background:radial-gradient(circle at 50% 40%,#c9a48a,#4d4a46)}
.review h4{left:154px;top:16px;font-weight:400;font-size:28px;color:var(--green)}
.review p{left:154px;top:68px;font-size:16.5px;line-height:22px;font-weight:300;width:570px}

/* footer */
.footer{left:107px;top:2959px;width:911px;height:96px;background:var(--darker);color:var(--white)}
.footer .touch{left:354px;top:14px;font-size:16px;font-weight:300}
.footer .touch span{color:var(--green-light)}
.footer .phone{left:475px;top:14px;font-size:16px;font-weight:300}
.footer .social{top:18px;font-size:12px;color:var(--green-light);display:flex;align-items:center;gap:5px}
.footer .social i{display:inline-block;width:10px;height:10px;border-radius:50%;background:var(--green-light)}
.footer .copy{left:0;width:911px;top:48px;text-align:center;font-size:8px;font-weight:300}
</style>
</head>
<body>
<div class="page">

  <header class="hero abs">
    <div class="hero-photo abs" role="img" aria-label="Dimmed photo of a tablet showing a bar chart beside a keyboard on a desk"></div>
    <div class="logo abs" style="left:94px;top:12px">L<b>O</b>GO</div>
    <nav class="nav">
      <a class="active" style="left:384px">HOME</a>
      <a style="left:468px">Clients&amp;Testimonials</a>
      <a style="left:664px">Services</a>
      <a style="left:770px">Contact</a>
    </nav>
    <h1 class="abs">Take the guesswork out of your<br>marketing strategy</h1>
    <p class="lead abs">Grow your e-commerce business and stay ahead of the competition.</p>
    <div class="cta abs"><span>Call now for a free consultation !!</span><span>(202) 555 0147</span></div>
  </header>

  <section class="newsletter abs" style="left:187px;top:393px;width:752px;height:165px">
    <div class="leaf abs" role="img" aria-label="Soft palm leaf decoration"></div>
    <h3>Subscribe to our newsletter</h3>
    <p>Sign up for our weekly newsletter to get the latest news, updates and amazing<br>offers delivered directly in your inbox</p>
    <div class="form"><div class="field">Enter your Email</div><div class="btn">Subscribe</div></div>
  </section>

  <section class="about abs">
    <h2 class="abs">ABOUT US</h2>
    <ul class="facts">
      <li style="top:116px">Our founder <span class="hl">Kostas Vranelis</span> is a digital marketer<br>&nbsp;&amp; an e-commerce expert since 2010.</li>
      <li style="top:172px">He has spoken to 20 different events around the world<br>up to 3,000 people in size.</li>
      <li style="top:227px">He has&nbsp; sold over 1500 training courses around e-commerce growth.</li>
      <li style="top:262px">He is&nbsp; the host of the Aegean Roundtable since 2017 - a high-level<br>networking event for 7 &amp; 8 figure entrepreneurs - 100 people<br>have come to Greece since 2017</li>
    </ul>
    <div class="snap abs" role="img" aria-label="Photo of the founder speaking on stage" style="left:575px;top:-10px;width:150px;height:130px;transform:rotate(14deg);background:linear-gradient(135deg,#e8efe9,#2f8a5a)"></div>
    <div class="snap abs" role="img" aria-label="Photo of the founder presenting to an audience" style="left:680px;top:75px;width:150px;height:140px;transform:rotate(10deg);background:linear-gradient(135deg,#b9a27a,#3a2a1a)"></div>
    <div class="snap abs" role="img" aria-label="Photo of the founder with a guest" style="left:525px;top:145px;width:150px;height:130px;transform:rotate(-12deg);background:linear-gradient(135deg,#8a6a4a,#3a2c22)"></div>
    <div class="snap abs" role="img" aria-label="Photo of a filmed interview in a studio" style="left:650px;top:235px;width:175px;height:115px;transform:rotate(28deg);background:linear-gradient(135deg,#e7e7e7,#7d8085)"></div>
  </section>

  <section class="offers abs">
    <h2>Your business, your success - <span>guaranteed.</span></h2>
    <h3>What we offer</h3>
    <div class="offer" style="left:2px">
      <svg width="48" height="40" viewBox="0 0 48 40"><rect x="2" y="8" width="44" height="30" rx="3" fill="#4f8a64"/><rect x="14" y="2" width="20" height="10" rx="2" fill="#4f8a64"/><rect x="34" y="20" width="12" height="10" rx="2" fill="#edf2ee"/><path d="M8 16h32" stroke="#edf2ee" stroke-width="2"/></svg>
      <h4>Paid ads<br>(Done for you)</h4>
      <p style="text-align:left;padding-left:7px">Our paid ads service is designed<br>to help businesses reach their target<br>audience through targeted advertising.</p>
    </div>
    <div class="offer" style="left:264px">
      <svg width="50" height="46" viewBox="0 0 50 46"><rect x="0" y="0" width="50" height="38" rx="6" fill="#4f8a64"/><path d="M18 38l6 8 6-8z" fill="#4f8a64"/><circle cx="14" cy="15" r="4" fill="#edf2ee"/><path d="M8 28c0-5 12-5 12 0" fill="#edf2ee"/><path d="M25 12h16M25 19h16M25 26h12" stroke="#edf2ee" stroke-width="3"/></svg>
      <h4>Consulting/Mastermind<br>(Done with you)</h4>
      <p>offering customized solutions tailored<br>to each client's specific needs and goals</p>
    </div>
    <div class="offer" style="left:511px">
      <svg width="44" height="46" viewBox="0 0 44 46"><rect x="8" y="2" width="34" height="40" fill="none" stroke="#4f8a64" stroke-width="3"/><path d="M20 12h16M20 19h16" stroke="#4f8a64" stroke-width="3"/><circle cx="10" cy="22" r="5" fill="#4f8a64"/><path d="M2 44v-10c0-4 4-6 8-6h10l8-6" stroke="#4f8a64" stroke-width="5" fill="none"/></svg>
      <h4 style="line-height:23px">Training<br>(Do it youself)</h4>
      <p style="text-align:left;padding-left:8px">you'll gain practical hands-on<br>experience that can be implemented<br>immediately in your own work.</p>
    </div>
    <div class="btn-green abs" style="left:315px;top:388px;width:157px;height:34px">Call us now!!</div>
  </section>

  <section class="cases abs">
    <h2 class="abs">Case studies</h2>
    <p class="intro abs">We have been collaborating with dozens of e-commerce stores on their growth<br>&amp; helped them scale to multiple 6, 7 &amp; 8 figures either on consulting</p>
    <div class="case" style="left:148px"><div class="img" role="img" aria-label="Photo of glass office towers against the sky" style="background:linear-gradient(160deg,#c9d6e2,#2b3036)"></div><h4>Lorem Ipsum</h4><p>Lorem ipsum dolor sit amet, consectetur adipiscing elit, sed do eiusmod tempor incidi-</p></div>
    <div class="case" style="left:365px"><div class="img" role="img" aria-label="Photo of two colleagues giving a high five at a desk" style="background:linear-gradient(160deg,#b98a6a,#e4e1dc)"></div><h4>Lorem Ipsum</h4><p>Lorem ipsum dolor sit amet, consectetur adipiscing elit, sed do eiusmod tempor incidi-</p></div>
    <div class="case" style="left:583px"><div class="img" role="img" aria-label="Photo of a woman reviewing charts on a laptop by a window" style="background:linear-gradient(160deg,#e3e7e3,#6f7f62)"></div><h4>Lorem Ipsum</h4><p>Lorem ipsum dolor sit amet, consectetur adipiscing elit, sed do eiusmod tempor incidi-</p></div>
    <div class="btn-green abs" style="left:377px;top:626px;width:155px;height:36px;font-size:17px">Read more</div>
  </section>

  <h2 class="clients-title abs">What our clients say about us</h2>

  <article class="review abs" style="top:2285px">
    <div class="avatar abs" role="img" aria-label="Client portrait"></div>
    <h4 class="abs">Lorem Ipsum</h4>
    <p class="abs">“Lorem ipsum dolor sit amet, consectetur adipiscing elit, sed do eiusmod tempor incididunt ut labore et dolore magna aliqua. Quis ipsum suspendisse ultrices gravida. Risus commodo vivera”</p>
  </article>
  <article class="review abs" style="top:2490px;left:185px">
    <div class="avatar abs" role="img" aria-label="Client portrait"></div>
    <h4 class="abs">Lorem Ipsum</h4>
    <p class="abs">“Lorem ipsum dolor sit amet, consectetur adipiscing elit, sed do eiusmod tempor incididunt ut labore et dolore magna aliqua. Quis ipsum suspendisse ultrices gravida. Risus commodo vivera”</p>
  </article>

  <section class="newsletter abs" style="left:107px;top:2718px;width:911px;height:173px">
    <div class="leaf abs" role="img" aria-label="Soft palm leaf decoration" style="width:140px"></div>
    <h3>Subscribe to our newsletter</h3>
    <p>Sign up for our weekly newsletter to get the latest news, updates and amazing<br>offers delivered directly in your inbox</p>
    <div class="form"><div class="field">Enter your Email</div><div class="btn">Subscribe</div></div>
  </section>

  <footer class="footer abs">
    <div class="logo abs" style="left:94px;top:16px">L<b>O</b>GO</div>
    <div class="touch abs"><span>Get</span> in touch</div>
    <div class="phone abs">(202) 555 0147</div>
    <div class="social abs" style="left:705px"><i></i>Connectly</div>
    <div class="social abs" style="left:790px"><i></i>Postwave</div>
    <div class="copy abs">copyright@growthdesk.example</div>
  </footer>

</div>
</body>
</html>
```